Website art for a private investigator.

The purposed graphic is for a business website ( corvashield.example ). The business name is “Halberd & Associates ltd.” This firm is a private investigation agency. The purposed graphic will be placed in the upper most main area of the main page of the website. If you look at the website now there is no graphic.

I have an idea of what I am looking for. I imagine a graphic depicting a contemporary private investigator walking through a dark alley searching for some unknown item. This is symbolic of private investigators hired to find information for people who their selfs do not have the know how nor could they handle the complexity and high stress environment. When I say contemporary I am referring to todays private investigators typically highly educated and well dressed.

Target Market(s)

People who need a private investigator

Industry/Entity Type

Business

Requirements
Must have
• match website; I have an idea of what I am looking for. I imagine a graphic depicting a contemporary private investigator walking through a dark alley searching for some unknown item. This is symbolic of private investigators hired to find information for people who their selfs do not have the know how nor could they handle the complexity and high stress environment. When I say contemporary I am referring to todays private investigators typically highly educated and well dressed.
Should not have
• Everyone please understand, I am not looking for a new website. I am only looking for the image. If you have submitted a design and its displayed on another website other than mine. I will not select your design. I am sorry for being harsh, but I asked for the image to match my website.

```html
<!DOCTYPE html>
<html lang="en">
<head>
<meta charset="utf-8">
<title>Halberd &amp; Associates ltd. — Private Investigations</title>
<link rel="stylesheet" href="https://fonts.googleapis.com/css2?family=Open+Sans:ital,wght@0,300;0,400;0,600;0,700;1,400&display=swap">
<style>
:root{
  --red:#dd4a36;
  --red-dark:#c93d2b;
  --blue:#2b8fd3;
  --ink:#2a2a2a;
  --grey:#7a7a7a;
  --dark:#1f1f1f;
  --footer:#2c2c2c;
  --band:#f1f1f1;
  --cream:#f7f4f1;
}
*{box-sizing:border-box;margin:0;padding:0}
html,body{width:1200px;height:2571px;overflow:hidden}
body{font-family:"Open Sans",Arial,sans-serif;color:var(--ink);background:#fff}
.wrap{position:relative;width:985px;margin:0 auto}
section,header,nav,footer{position:relative;width:1200px}

.site-header{height:86px;background:#fff}
.brand{position:absolute;left:115px;top:22px;font-size:34px;font-weight:600;color:var(--blue);letter-spacing:-.5px}
.social{position:absolute;right:100px;top:14px;display:flex;gap:10px}
.social span{width:16px;height:16px;border-radius:50%;background:#555}
.toll{position:absolute;right:100px;top:46px;font-size:15px;color:#555}
.toll b{color:var(--red);font-size:19px;font-weight:600}

.main-nav{height:40px;background:var(--red)}
.main-nav ul{list-style:none;position:relative;width:1200px;height:40px}
.main-nav li{position:absolute;top:0;height:40px;line-height:40px;color:#fff;font-size:15px}
.main-nav li.active{background:var(--blue);padding:0 30px;left:128px}

.hero{height:446px;background:radial-gradient(ellipse at 70% 25%,#6b6b6b 0%,#2e2e2e 35%,#101010 75%)}
.hero .arrow{position:absolute;top:200px;width:46px;height:46px;border-radius:50%;background:rgba(255,255,255,.25)}
.hero .arrow.prev{left:12px}.hero .arrow.next{right:12px}
.hero svg{position:absolute;top:15px}

.welcome{height:348px;background:#fff}
.welcome .figure{position:absolute;left:115px;top:28px;width:370px;height:320px;background:linear-gradient(180deg,#e9e9e9,#8a8a8a 60%,#3a3a3a)}
.section-title{font-weight:300;font-size:40px;letter-spacing:.5px;text-transform:uppercase}
.section-title em{font-style:normal;color:var(--red)}
.welcome .section-title{position:absolute;left:515px;top:90px}
.welcome p{position:absolute;left:515px;top:150px;width:585px;font-size:13px;line-height:21px;color:var(--grey)}

.eyes{height:180px;background:var(--band)}
.eyes h2{position:absolute;left:130px;top:48px;font-size:54px;font-weight:300;color:var(--red);letter-spacing:1px}
.eyes p{position:absolute;left:135px;top:118px;font-size:14px;color:var(--grey)}
.hire{position:absolute;left:848px;top:51px;display:flex;height:83px}
.hire .icon{width:83px;background:#3a3a3a;display:flex;align-items:center;justify-content:center}
.hire .label{width:166px;background:var(--red);color:#fff;font-size:24px;display:flex;align-items:center;justify-content:center;gap:0}

.what{height:371px;background:linear-gradient(90deg,#161616,#242424 60%,#1b1b1b);color:#ddd}
.what .section-title{position:absolute;left:115px;top:30px;color:#fff}
.what .body{position:absolute;left:115px;top:100px;width:985px;font-size:14px;line-height:22px}
.what .body p+p{margin-top:22px}

.charge{height:372px;background:linear-gradient(180deg,#f2efec,#fbfaf9)}
.charge .section-title{position:absolute;left:115px;top:72px}
.charge .body{position:absolute;left:115px;top:140px;width:985px;font-size:14px;line-height:22px;color:#333}
.charge .body p+p{margin-top:12px}

.cta{height:123px;background:var(--red);color:#fff;text-align:center;line-height:123px;font-size:36px;font-weight:400}
.cta b{font-weight:600;font-size:42px}

.testimonial{height:291px;background:var(--cream)}
.testimonial .mark{position:absolute;left:128px;top:40px;font-size:70px;color:#555;font-family:Georgia,serif}
.testimonial blockquote{position:absolute;left:150px;top:70px;width:790px;font-size:14px;line-height:22px;color:var(--grey);font-style:italic}
.testimonial .avatar{position:absolute;left:952px;top:55px;width:124px;height:124px;border-radius:50%;background:radial-gradient(circle at 50% 40%,#f1d5c2,#c9a684 70%);border:4px solid #fff}
.testimonial cite{position:absolute;right:323px;top:190px;font-style:normal;color:var(--red);font-size:15px;letter-spacing:1px}

.site-footer{height:251px;background:var(--footer);color:#aaa;font-size:12px;line-height:18px}
.site-footer h4{color:#fff;font-size:14px;font-weight:600;text-transform:uppercase;margin-bottom:16px}
.col{position:absolute;top:44px}
.col.about{left:126px;width:300px}
.col.analysis{left:577px;width:280px}
.col.analysis li{list-style:none;border-bottom:1px solid #444;padding:4px 0}
.col.posts{left:937px;width:180px}
.copyright{height:63px;background:#ece8e4;text-align:center;line-height:63px;font-size:12px;color:#555}
</style>
</head>
<body>
<header class="site-header">
  <div class="brand">Corvashield</div>
  <div class="social"><span></span><span></span><span></span><span></span></div>
  <div class="toll">Call Toll Free: <b>(555) 014-2783</b></div>
</header>

<nav class="main-nav">
  <ul>
    <li class="active">Home</li>
    <li style="left:290px">About Us</li>
    <li style="left:440px">Main</li>
    <li style="left:565px">Our Services</li>
    <li style="left:740px">Investigations &amp; Analysis</li>
    <li style="left:1000px">Contacts</li>
  </ul>
</nav>

<section class="hero" role="img" aria-label="Investigator with a flashlight walking through a dark, smoky alley under a fire escape">
  <span class="arrow prev"></span><span class="arrow next"></span>
</section>

<section class="welcome">
  <div class="figure" role="img" aria-label="Man in a suit looking through binoculars"></div>
  <h1 class="section-title">Welcome to <em>Corvashield</em></h1>
  <p>We are a licensed investigation agency serving private clients, attorneys and businesses who need clear facts fast. Our team works quietly and thoroughly, gathering evidence, locating people and verifying records with discretion. Every case is handled by experienced professionals who report findings in plain, usable form. We listen first, plan carefully and keep you informed from the first call to the final report, so that you can make confident decisions.</p>
</section>

<section class="eyes">
  <h2>WE'LL BE YOUR EYES!</h2>
  <p>Discreet, careful work for every client we serve.</p>
  <div class="hire">
    <div class="icon">
      <svg width="30" height="30" viewBox="0 0 24 24" fill="#fff"><path d="M2 10h4v12H2zM8 21V10l5-8c1.5 0 2.5 1 2.2 2.5L14.5 9H21c1.2 0 2 1 1.8 2.2l-1.6 8.2c-.2 1-1 1.6-2 1.6z"/></svg>
    </div>
    <div class="label">HIRE US!</div>
  </div>
</section>

<section class="what">
  <h2 class="section-title">What <em>we do</em></h2>
  <div class="body">
    <p>Halberd &amp; Associates' private investigators are available for immediate service throughout southern Ohio and the surrounding areas. Service is immediately available in West Virginia and neighbouring counties. Full investigative support is available to the general public involving criminal and civil matters, and private investigators are available to provide full support to attorneys involved in criminal defense and civil litigation.</p>
    <p>Halberd &amp; Associates private investigators are always easily obtainable for the general public. We keep our fees reasonable and never charge for travel. This makes us available to you without unnecessary expense. Investigative and analysis services are available by the hour or for a flat rate. Click here for our fees.</p>
  </div>
</section>

<section class="charge">
  <h2 class="section-title">How much <em>do we charge</em></h2>
  <div class="body">
    <p>We believe the services of a private investigator should be obtainable and reasonable to the general public. The fees charged by Halberd &amp; Associates are low compared to other similar firms. For one, we do not charge for travel. This makes us available to you without unnecessary expense. Investigative and analysis services are available by the hour or at a flat rate. See the private investigator fees for more information.</p>
    <p>Our investigative and analysis ability is based on the application of Structured Analysis and Expert Judgement. The use of these methods allows us to provide clients of Halberd &amp; Associates with objective results. In the areas of reconstructing past events, evaluating the credibility of evidence and witness testimony, processing of abstract information derived from multiple portals, and making analytical judgements based on available subject matter information. In turn, we are not only able to provide investigative service, but full analysis support to clients.</p>
  </div>
</section>

<section class="cta">Call For A Free Consultation <b>(555) 014-2783</b></section>

<section class="testimonial">
  <span class="mark">“</span>
  <blockquote>Our experience and unbiased approach is your greatest strength! If you are an attorney, company, or private individual with a legal need we will provide you with accurate, timely and unbiased information that will help you make an informed decision, mitigate risk, and resolve problems.</blockquote>
  <div class="avatar" role="img" aria-label="Client portrait"></div>
  <cite>LENA MARSH</cite>
</section>

<footer class="site-footer">
  <div class="col about">
    <h4>Veltris</h4>
    <p>Halberd &amp; Associates ltd. provides civil and criminal investigation services. Private investigators are available for immediate service in Ohio throughout the region. Service is immediately available in West Virginia throughout the nearby cities and surrounding areas.</p>
  </div>
  <div class="col analysis">
    <h4>Analysis of Information</h4>
    <ul>
      <li>Application of Structured Analysis</li>
      <li>Discovery file analysis</li>
      <li>Threat analysis: person, supply line and structures</li>
      <li>Other assignments accepted on limited bases</li>
    </ul>
  </div>
  <div class="col posts">
    <h4>Recent Posts</h4>
    <p>P.O. Box 412<br>Lakeford, Ohio 45612<br><br>Ohio License: 0000000<br>West Virginia License: 0000<br>Private Investigations Firm</p>
  </div>
</footer>

<div class="copyright">© 2015 Halberd &amp; Associates ltd. All rights reserved.</div>
</body>
</html>
```